Logo and Business Card Design

We are macadamia farmers with a network of operations able to deliver macadamia nuts to you!
Be it wholesale or retail supply, our production capacity, network of farms and processing facilities is able to provide reliable and secure supply of macadamia products.
We have a network of owned and contract production macadamia farms located throughout Queensland and New South Wales. Our farms are located in the lush green hinterland area of Northern New south wales and the rich and productive farmlands of the Burnett area of southern Queensland. We pride ourselves on our environmentally sensitive production systems, the ownership and pride in which our network of farmers care for their orchards and the food we produce. Collectively our farms deliver to processing facilities able to provide macadamia nut in shell and kernel in wholesale and retail quantities.
Our point of difference is our integrated supply chain, delivering paddock to plate capacity.
The enterprise is a true network in that we have combined production, processing and marketing expertise into a one stop shop!
Our design should communicate our network capacity, we are a food producer which is respectful of the land and the environment in which we operate.
Our focus is Macadamia nut production, we farm and process Macadamia's where they are a native tree.

The draft design concept we feel is too mechanical and sterile, its time for something fresh and exciting!

Environment

Pell Orchard Pty. Ltd
An Integrated Macadamia production Enterprise.

```html
<!DOCTYPE html>
<html lang="en">
<head>
<meta charset="utf-8">
<title>Pell Orchard — Business Card</title>
<link href="https://fonts.googleapis.com/css2?family=Exo+2:wght@400;600;800&display=swap" rel="stylesheet">
<style>
  :root{
    --bg:#e7e5e2;
    --paper:#ffffff;
    --earth:#472a16;
    --leaf:#13a048;
    --ink-light:#f3ece6;
  }
  *{margin:0;padding:0;box-sizing:border-box}
  html,body{width:1200px;height:901px;overflow:hidden;background:var(--bg)}
  body{position:relative;font-family:"Exo 2",sans-serif}
  .card{
    position:absolute;top:299px;width:530px;height:303px;
    border-radius:26px;overflow:hidden;background:var(--paper);
    box-shadow:0 6px 18px rgba(0,0,0,.18);
  }
  .card--front{left:50px}
  .card--back{left:620px}
  .card__shape{position:absolute;inset:0}
  .brand{
    position:absolute;display:flex;align-items:center;gap:10px;
    color:var(--earth);font-weight:800;letter-spacing:.02em;text-transform:uppercase;
  }
  .brand__dot{border-radius:50%;background:var(--leaf);flex:none}
  .card--front .brand{left:40px;top:92px;font-size:30px}
  .card--front .brand__dot{width:16px;height:16px}
  .card--back .brand{left:0;right:0;top:0;bottom:0;justify-content:center;font-size:50px}
  .card--back .brand__dot{width:24px;height:24px}
  .contact{
    position:absolute;left:325px;right:28px;top:136px;
    color:var(--ink-light);font-size:11px;line-height:15px;
  }
  .contact__name{font-size:15px;font-weight:600;letter-spacing:.04em;text-transform:uppercase;line-height:18px}
  .contact__role{margin-bottom:7px}
  .contact__address{margin-bottom:7px}
  .contact__row{display:flex;justify-content:space-between;align-items:center}
  .contact__icon{width:10px;height:10px;flex:none}
</style>
</head>
<body>

<section class="card card--front" aria-label="Business card front">
  <svg class="card__shape" viewBox="0 0 530 303" preserveAspectRatio="none" aria-hidden="true">
    <rect width="530" height="303" fill="var(--earth)"/>
    <path d="M0,0 H530 V49 C330,74 200,229 0,226 Z" fill="var(--leaf)"/>
    <path d="M0,0 H530 V35 C330,60 200,215 0,210 Z" fill="var(--paper)"/>
  </svg>
  <div class="brand"><span class="brand__dot"></span>Pell Orchard</div>
  <div class="contact">
    <div class="contact__name">Dana Whitfield</div>
    <div class="contact__role">Managing Director</div>
    <div class="contact__address">41 Level 2 Arcade<br>Hillside Road QLD</div>
    <div class="contact__row"><span>012 555 0142</span>
      <svg class="contact__icon" viewBox="0 0 10 10"><path d="M2 1l2 2-1 1.2c.6 1.2 1.5 2.1 2.8 2.8L7 6l2 2-1.3 1.3C4.5 9 1 5.5.7 2.3z" fill="currentColor"/></svg></div>
    <div class="contact__row"><span>012 555 0143</span>
      <svg class="contact__icon" viewBox="0 0 10 10"><rect x="2.5" y=".5" width="5" height="9" rx="1" fill="none" stroke="currentColor"/></svg></div>
    <div class="contact__row"><span>012 555 0144</span>
      <svg class="contact__icon" viewBox="0 0 10 10"><rect x="1" y="4" width="8" height="5" fill="currentColor"/><rect x="3" y="1" width="4" height="3" fill="none" stroke="currentColor"/></svg></div>
    <div class="contact__row"><span>hello@pellorchard.com</span>
      <svg class="contact__icon" viewBox="0 0 10 10"><rect x=".5" y="2" width="9" height="6" fill="none" stroke="currentColor"/><path d="M.5 2l4.5 3.5L9.5 2" fill="none" stroke="currentColor"/></svg></div>
    <div class="contact__row"><span>www.pellorchard.com</span>
      <svg class="contact__icon" viewBox="0 0 10 10"><circle cx="5" cy="5" r="4.3" fill="none" stroke="currentColor"/><path d="M.7 5h8.6M5 .7c-2.4 2.6-2.4 6 0 8.6M5 .7c2.4 2.6 2.4 6 0 8.6" fill="none" stroke="currentColor" stroke-width=".8"/></svg></div>
  </div>
</section>

<section class="card card--back" aria-label="Business card back">
  <div class="brand"><span class="brand__dot"></span>Pell Orchard</div>
</section>

</body>
</html>
```